Summit Guest Partners

An Editable Business Card Template For SGP & SGH
Similar or Different Design

418 W. Marlow Ridge Pkwy.
Suite 2230
Irving, TX 75038

```html
<!DOCTYPE html>
<html lang="en">
<head>
<meta charset="utf-8">
<title>Summit Guest Partners – Business Card</title>
<link rel="stylesheet" href="https://fonts.googleapis.com/css2?family=Arimo:wght@400;700&display=swap">
<style>
  :root {
    --backdrop: #e6e6e6;
    --brand-red: #8f1b1f;
    --brand-red-light: #9a2328;
    --paper: #f7f7f8;
    --ink-grey: #555559;
    --white: #ffffff;
  }
  * { margin: 0; padding: 0; box-sizing: border-box; }
  html, body { width: 1200px; height: 1200px; overflow: hidden; }
  body {
    background: var(--backdrop);
    font-family: "Arimo", Arial, sans-serif;
    position: relative;
  }
  .card {
    position: absolute;
    left: 262px;
    width: 686px;
    height: 392px;
    border-radius: 22px;
    overflow: hidden;
  }
  .card-front {
    top: 165px;
    background: linear-gradient(160deg, var(--brand-red-light), var(--brand-red));
    color: var(--white);
  }
  .card-back {
    top: 653px;
    background: var(--paper);
  }
  .divider-rule {
    position: absolute; left: 59px; right: 59px; top: 190px;
    height: 3px; background: var(--white); border-radius: 2px;
  }
  .holder-name {
    position: absolute; left: 59px; top: 54px;
    font-size: 29px; font-weight: 700; letter-spacing: 0.2px;
  }
  .holder-title {
    position: absolute; left: 59px; top: 88px;
    font-size: 18px; font-weight: 400;
  }
  .address {
    position: absolute; left: 60px; top: 232px;
    font-size: 15.5px; line-height: 19px;
  }
  .contact-list {
    position: absolute; left: 60px; top: 286px;
    list-style: none; font-size: 15.5px;
  }
  .contact-list li {
    display: flex; align-items: center; height: 19px;
  }
  .contact-list svg { width: 15px; height: 15px; margin-right: 10px; fill: var(--white); }
  .tagline {
    position: absolute; left: 408px; top: 286px; width: 220px;
    text-align: center; font-size: 21px; font-weight: 700; line-height: 26px;
  }
  .back-headline {
    position: absolute; left: 42px; top: 63px;
    color: var(--brand-red); font-size: 21px; font-weight: 700; line-height: 26px;
  }
  .benefit-list {
    position: absolute; left: 38px; top: 148px; list-style: none;
    color: var(--ink-grey); font-size: 15.5px;
  }
  .benefit-list li {
    display: flex; align-items: center; height: 38.7px;
  }
  .benefit-list svg { width: 20px; height: 20px; margin-right: 12px; }
  .brand-dot {
    position: absolute; left: 376px; top: 126px;
    width: 168px; height: 168px; border-radius: 50%;
    background: var(--brand-red);
  }
  .brand-name {
    position: absolute; left: 560px; top: 172px;
    color: var(--brand-red); font-size: 21px; font-weight: 700; line-height: 26px;
  }
</style>
</head>
<body>

<section class="card card-front">
  <span class="divider-rule"></span>
  <h1 class="holder-name">Dana Whitfield</h1>
  <p class="holder-title">Sales Manager</p>
  <p class="address">418 W. Marlow Ridge Pkwy.<br>Suite 2230, Irving, TX 75038</p>
  <ul class="contact-list">
    <li><svg viewBox="0 0 16 16"><path d="M3.5 1l2.4 3-1.4 1.6c.8 1.9 2.3 3.4 4.2 4.3l1.6-1.4 3 2.4-1.4 2.4C6.8 13.4 2.6 9.2 1.1 2.5z"/></svg>214-555-0147</li>
    <li><svg viewBox="0 0 16 16"><path d="M4 1h8v14H4zM5.5 2.5v9.5h5V2.5zM7.3 13h1.4v1H7.3z" fill-rule="evenodd"/></svg>480-555-0192</li>
    <li><svg viewBox="0 0 16 16"><path d="M1 4h14v9H1z"/><path d="M1.5 4.5 8 9.5l6.5-5" stroke="#8f1b1f" stroke-width="1.2" fill="none"/></svg>DWhitfield@summitguest.com</li>
    <li><svg viewBox="0 0 16 16"><circle cx="8" cy="8" r="7"/><path d="M1 8h14M8 1c-3 3-3 11 0 14M8 1c3 3 3 11 0 14" stroke="#8f1b1f" stroke-width="1" fill="none"/></svg>SGPOilField.com</li>
  </ul>
  <p class="tagline">Oil Field<br>Housingon Auropilot</p>
</section>

<section class="card card-back">
  <h2 class="back-headline">Experienced Provider To Oil, Gas,<br>Energy &amp; Construction Industries</h2>
  <ul class="benefit-list">
    <li><svg viewBox="0 0 20 20"><path d="M16.5 8.5A7 7 0 1 1 13 3.9" fill="none" stroke="#8f1b1f" stroke-width="2.2"/><path d="M6 9.5l3.5 3.5L18 3.5" fill="none" stroke="#8f1b1f" stroke-width="2.4"/></svg>Consolidated Billing</li>
    <li><svg viewBox="0 0 20 20"><path d="M16.5 8.5A7 7 0 1 1 13 3.9" fill="none" stroke="#8f1b1f" stroke-width="2.2"/><path d="M6 9.5l3.5 3.5L18 3.5" fill="none" stroke="#8f1b1f" stroke-width="2.4"/></svg>Full Service Corporate Lodging</li>
    <li><svg viewBox="0 0 20 20"><path d="M16.5 8.5A7 7 0 1 1 13 3.9" fill="none" stroke="#8f1b1f" stroke-width="2.2"/><path d="M6 9.5l3.5 3.5L18 3.5" fill="none" stroke="#8f1b1f" stroke-width="2.4"/></svg>Live Customer Support 24/7/365</li>
    <li><svg viewBox="0 0 20 20"><path d="M16.5 8.5A7 7 0 1 1 13 3.9" fill="none" stroke="#8f1b1f" stroke-width="2.2"/><path d="M6 9.5l3.5 3.5L18 3.5" fill="none" stroke="#8f1b1f" stroke-width="2.4"/></svg>Proven Track Record&nbsp; Of Performance</li>
    <li><svg viewBox="0 0 20 20"><path d="M16.5 8.5A7 7 0 1 1 13 3.9" fill="none" stroke="#8f1b1f" stroke-width="2.2"/><path d="M6 9.5l3.5 3.5L18 3.5" fill="none" stroke="#8f1b1f" stroke-width="2.4"/></svg>Best Negotiated Rates &amp; No Additional Fees</li>
  </ul>
  <span class="brand-dot"></span>
  <span class="brand-name">Summit<br>Guest<br>Partners</span>
</section>

</body>
</html>
```